Website Revamp: Favorzo.com

Just got a new logo looking for a web design to go with the business. I need the photoshop files and stock photos. No Word Press Please.

```html
<!DOCTYPE html>
<html lang="en">
<head>
<meta charset="utf-8">
<title>Favorzo.com — Auto Recycling</title>
<link rel="stylesheet" href="https://fonts.googleapis.com/css2?family=Roboto:wght@400;500;700;900&family=Lato:wght@400;700&display=swap">
<style>
:root{
  --green:#5ea91f;
  --green-bright:#74c230;
  --orange:#f0561c;
  --ink:#1f1f1f;
  --muted:#5a5a5a;
  --soft:#eff0ec;
  --soft2:#f2f2f2;
  --footer:#1b1b1b;
  --white:#fff;
}
*{box-sizing:border-box;margin:0;padding:0}
html,body{width:1200px;height:3158px;overflow:hidden}
body{position:relative;background:var(--white);font-family:"Lato",sans-serif;color:var(--ink)}
.abs{position:absolute}
h2.section-title{position:absolute;left:0;width:1200px;text-align:center;font-family:"Roboto",sans-serif;font-weight:900;font-size:38px;letter-spacing:-.3px;color:var(--ink)}
.section-sub{position:absolute;left:0;width:1200px;text-align:center;font-size:13.5px;color:#444}

/* header */
.site-header{position:absolute;left:0;top:0;width:1200px;height:92px;background:var(--white)}
.brand{position:absolute;left:93px;top:30px;display:flex;align-items:center;gap:10px;font-family:"Roboto",sans-serif;font-weight:900;font-size:24px;color:var(--green)}
.brand-dot{width:34px;height:34px;border-radius:50%;background:var(--green)}
.contact-top{position:absolute;left:935px;top:10px;display:flex;gap:8px;align-items:center}
.contact-top .phone-dot{width:30px;height:30px;border-radius:50%;background:var(--green-bright);display:flex;align-items:center;justify-content:center}
.contact-top b{display:block;font-size:14.5px;font-weight:700;color:var(--ink)}
.contact-top span{display:block;font-size:11.5px;color:#333}
.main-nav{position:absolute;top:68px;right:92px;display:flex;gap:41px;font-family:"Roboto",sans-serif;font-size:11.5px;color:#333}
.main-nav .active{color:var(--green)}

/* hero */
.hero{position:absolute;left:0;top:92px;width:1200px;height:508px;background:radial-gradient(ellipse at 28% 18%,#d9ddd2 0%,#8c9488 28%,#3d4540 55%,#1d2320 100%)}
.hero-curve{position:absolute;left:0;top:520px}
.hero-copy{position:absolute;left:92px;top:252px;color:var(--white)}
.hero-copy .kicker{font-family:"Roboto",sans-serif;font-size:25px;font-weight:400}
.hero-copy h1{font-family:"Roboto",sans-serif;font-weight:900;font-size:45px;line-height:50px;margin-top:2px}
.hero-copy h1 em{font-style:normal;color:var(--green-bright);display:block}
.hero-copy p{font-size:14px;line-height:20px;margin-top:8px;width:360px}
.btn{position:absolute;display:flex;align-items:center;justify-content:center;font-family:"Lato",sans-serif;font-weight:700;font-size:12px;color:var(--white);text-transform:uppercase}
.btn-green{background:var(--green)}
.btn-dark{background:#1d1d1d}

/* steps */
.step{position:absolute;top:768px;width:300px;text-align:center}
.step svg{display:block;margin:0 auto}
.step-label{margin-top:14px;font-weight:700;font-size:13.5px;color:#222}
.step-label em{font-style:normal;color:var(--green)}

/* offers */
.offers{position:absolute;left:0;top:1011px;width:1200px;height:543px;background:var(--soft)}
.car-card{position:absolute;top:1152px;width:238px;height:260px;background:var(--white);box-shadow:0 1px 6px rgba(0,0,0,.18)}
.car-photo{position:absolute;left:5px;top:6px;width:228px;height:139px}
.car-card h3{position:absolute;left:12px;top:160px;font-family:"Roboto",sans-serif;font-weight:500;font-size:19px;color:#222;white-space:nowrap}
.car-card .loc{position:absolute;left:12px;top:184px;font-size:13px;color:#555}
.car-card .price{position:absolute;left:12px;top:213px;width:72px;height:28px;border-radius:14px;background:var(--green);color:#fff;font-weight:700;font-size:12.5px;display:flex;align-items:center;justify-content:center}
.slider-arrow{position:absolute;top:1267px;width:32px;height:32px;border-radius:50%;background:#fff;box-shadow:0 1px 4px rgba(0,0,0,.2);display:flex;align-items:center;justify-content:center}

/* difference */
.timeline-line{position:absolute;left:599px;top:1804px;height:320px;border-left:1px dashed #999}
.tl-num{position:absolute;width:46px;height:46px;border-radius:50%;background:var(--orange);color:#fff;font-weight:700;font-size:13.5px;display:flex;align-items:center;justify-content:center}
.feature h3{font-family:"Roboto",sans-serif;font-weight:500;font-size:22px;color:#222}
.feature p{font-size:13px;line-height:20px;color:#555;margin-top:10px}
.feature{position:absolute}
.feature.right{left:641px;width:460px}
.feature.left{left:100px;width:457px;text-align:right}

/* testimonials */
.excellence{position:absolute;left:0;top:2366px;width:1200px;height:407px;background:var(--soft2)}
.review{position:absolute;top:2497px;width:316px;height:206px;background:#fff;border-radius:22px 22px 4px 22px;box-shadow:0 1px 6px rgba(0,0,0,.12);padding:24px 17px}
.review h3{font-family:"Roboto",sans-serif;font-weight:500;font-size:19px;line-height:22px;color:#222}
.review p{font-size:13px;line-height:21px;color:#555;margin-top:10px;padding-left:1px;padding-right:4px}
.review .meta{margin-top:14px;display:flex;align-items:center;gap:4px;font-size:9.5px;color:#555}
.review.featured{background:var(--green);box-shadow:none}
.review.featured h3,.review.featured p{color:#fff}
.review.featured .meta{color:#b8e08f}
.stars{color:#f5b800;letter-spacing:2px;font-size:12px}

/* footer */
.site-footer{position:absolute;left:0;top:2773px;width:1200px;height:385px;background:var(--footer);color:#c9c9c9}
.f-col{position:absolute;top:70px}
.f-col h4{font-family:"Roboto",sans-serif;font-weight:500;font-size:18px;color:#fff;margin-bottom:12px}
.f-col li{list-style:none;font-size:11.5px;line-height:27px}
.f-contact{display:flex;gap:7px;font-size:11.5px;line-height:15px;margin-bottom:18px}
.field{position:absolute;background:#fff;color:#444;font-size:10px;padding:9px 9px}
.socials{position:absolute;top:264px;left:542px;display:flex;gap:6px}
.socials span{width:24px;height:24px;border-radius:50%;background:#fff}
.copyright{position:absolute;top:303px;left:0;width:1200px;text-align:center;font-size:10px;color:#fff}
.copyright em{font-style:normal;color:var(--green-bright)}
</style>
</head>
<body>

<header class="site-header">
  <div class="brand"><span class="brand-dot"></span>Favorzo</div>
  <div class="contact-top">
    <span class="phone-dot"><svg width="14" height="14" viewBox="0 0 24 24"><path fill="#fff" d="M6.6 10.8a15 15 0 0 0 6.6 6.6l2.2-2.2c.3-.3.7-.4 1-.2 1.1.4 2.3.6 3.6.6.6 0 1 .4 1 1V20c0 .6-.4 1-1 1A17 17 0 0 1 3 4c0-.6.4-1 1-1h3.5c.6 0 1 .4 1 1 0 1.3.2 2.5.6 3.6.1.3 0 .7-.2 1z"/></svg></span>
    <div><b>+1 (555) 014 2297</b><span>hello@favorzo.com</span></div>
  </div>
  <nav class="main-nav"><span class="active">HOME</span><span>ABOUT US</span><span>SERVICE</span><span>CONTACT US</span></nav>
</header>

<section class="hero" role="img" aria-label="Dark sports car parked on a cobblestone driveway under trees in soft morning light"></section>
<svg class="hero-curve" width="1200" height="82" viewBox="0 0 1200 82"><path d="M0 20 Q600 140 1200 0 L1200 82 L0 82Z" fill="#fff"/></svg>
<div class="hero-copy">
  <div class="kicker">FILL OUT OUR FROM</div>
  <h1>FOR AN INSTANT<em>OFFER</em></h1>
  <p>We don't Sell your information, We will only contact you about your car</p>
</div>
<div class="btn btn-green" style="left:94px;top:444px;width:103px;height:34px">Get an offer</div>

<h2 class="section-title" style="top:660px">HOW IT WORK</h2>
<p class="section-sub" style="top:711px">If you use this site regularly and would like to help keep the site on the Internet</p>

<div class="step" style="left:111px">
  <svg width="146" height="146" viewBox="0 0 146 146"><circle cx="73" cy="73" r="64" fill="none" stroke="#74c230" stroke-width="8"/><rect x="45" y="48" width="56" height="48" rx="10" fill="#f0561c" role="img" aria-label="Car icon"/><text x="24" y="54" fill="#74c230" font-family="Lato" font-size="14">01</text></svg>
  <div class="step-label">TELL US ABOUT YOUR VEHICLE</div>
</div>
<div class="step" style="left:449px">
  <svg width="146" height="146" viewBox="0 0 146 146"><circle cx="73" cy="73" r="64" fill="none" stroke="#74c230" stroke-width="8"/><rect x="48" y="42" width="50" height="58" rx="8" fill="#f0561c" role="img" aria-label="Tow truck icon"/><text x="24" y="54" fill="#74c230" font-family="Lato" font-size="14">02</text></svg>
  <div class="step-label">WE PICK IT UO FOR <em>FREE!</em></div>
</div>
<div class="step" style="left:788px">
  <svg width="146" height="146" viewBox="0 0 146 146"><circle cx="73" cy="73" r="64" fill="none" stroke="#74c230" stroke-width="8"/><rect x="48" y="42" width="50" height="58" rx="8" fill="#f0561c" role="img" aria-label="Hand holding cash icon"/><text x="24" y="54" fill="#74c230" font-family="Lato" font-size="14">03</text></svg>
  <div class="step-label">WE GIVE YOU CASH!</div>
</div>

<section class="offers"></section>
<h2 class="section-title" style="top:1058px">CASH OFFER MADE DAILY!</h2>
<p class="section-sub" style="top:1109px">Receive cash on the spot for your vehicle! It doesn't matter how bad of shape it is in, we'll take it!</p>

<div class="slider-arrow" style="left:31px"><svg width="8" height="10"><path d="M6 1 2 5l4 4" stroke="#333" fill="none" stroke-width="1.5"/></svg></div>
<div class="slider-arrow" style="left:1137px"><svg width="8" height="10"><path d="M2 1l4 4-4 4" stroke="#333" fill="none" stroke-width="1.5"/></svg></div>

<article class="car-card" style="left:93px"><div class="car-photo" role="img" aria-label="Blue hatchback in a dark garage" style="background:linear-gradient(180deg,#1c2230,#2f7fd0 60%,#1a1c22)"></div><h3>2011 Norwell Avessa</h3><div class="loc">Providence, RI</div><div class="price">$280</div></article>
<article class="car-card" style="left:353px"><div class="car-photo" role="img" aria-label="Black coupe on a road under an overcast sky" style="background:linear-gradient(180deg,#cfd6d8,#8a9389 45%,#1e2024 70%,#5d5e58)"></div><h3>2008 Brisko Talvane</h3><div class="loc">Bothell, WA</div><div class="price">$210</div></article>
<article class="car-card" style="left:612px"><div class="car-photo" role="img" aria-label="Teal sports car in a desert at dusk" style="background:linear-gradient(180deg,#c47a44,#8a5a3a 40%,#1f7fa3 65%,#6e4a32)"></div><h3>2006 Brisko Korrimar</h3><div class="loc">Eugene, OR</div><div class="price">$315</div></article>
<article class="car-card" style="left:870px"><div class="car-photo" role="img" aria-label="Green classic muscle car at a shipping yard" style="background:linear-gradient(180deg,#b9c2c8,#8b7f6a 45%,#3f5a2f 70%,#4a4640)"></div><h3>2012 Vantor Quellis</h3><div class="loc">Portland, ME</div><div class="price">$595</div></article>

<div class="btn btn-dark" style="left:506px;top:1455px;width:188px;height:42px">Cash for my car now</div>

<h2 class="section-title" style="top:1615px">THE FAVORZO DIFFERENCE</h2>
<p class="section-sub" style="top:1667px">Sed ut perspiciatis unde omnis iste natus error sit voluptatem accusantium doloremque</p>

<div class="timeline-line"></div>
<div class="tl-num" style="left:576px;top:1781px">01</div>
<div class="tl-num" style="left:576px;top:1941px">02</div>
<div class="tl-num" style="left:576px;top:2100px">03</div>

<svg class="abs" style="left:641px;top:1728px" width="54" height="58" viewBox="0 0 54 58" role="img" aria-label="Cash payment icon"><rect x="4" y="30" width="40" height="8" fill="#5ea91f"/><rect x="0" y="44" width="44" height="12" fill="#5ea91f"/><path d="M18 28 L40 4 L52 8 L30 30Z" fill="#5ea91f"/></svg>
<div class="feature right" style="top:1788px"><h3>Cash On The Spot</h3><p>Offering check, PayQuick®, SendLane®, or CoinPost® instant transfers for your car! Of course, we also offer a standard check as well. Our professional drivers will hand deliver your check.</p></div>

<svg class="abs" style="left:284px;top:1896px" width="38" height="44" viewBox="0 0 38 44" role="img" aria-label="Document icon"><path d="M0 0h26l12 12v32H0z" fill="#5ea91f"/><path d="M8 18h22M8 25h22M8 32h22" stroke="#fff" stroke-width="3"/></svg>
<div class="feature left" style="top:1947px"><h3>Professional Title Handlers</h3><p>Have an issue with the title? No Problem. Our certified, professional drivers are well trained and can help you transfer that title in no time. We've been doing this quite a while.</p></div>

<svg class="abs" style="left:641px;top:2053px" width="50" height="43" viewBox="0 0 50 43" role="img" aria-label="Car icon"><path d="M8 16 L13 3h24l5 13h4v18h-5v8h-7v-8H15v8H8v-8H3V16z" fill="#5ea91f"/><rect x="15" y="7" width="20" height="8" fill="#fff"/><circle cx="11" cy="25" r="3" fill="#fff"/><circle cx="39" cy="25" r="3" fill="#fff"/></svg>
<div class="feature right" style="top:2106px"><h3>We Buy All Car Types</h3><p>Every scrap car has value, even if you might not think so. We're happy to take them off your hands and recycle them. Saving our planet is a priority and one less car wasting away helps!</p></div>

<div class="btn btn-green" style="left:506px;top:2253px;width:188px;height:40px">Hire a professional</div>

<section class="excellence"></section>
<h2 class="section-title" style="top:2423px">COMMITTED TO EXCELLENCE</h2>

<article class="review" style="left:93px"><h3>Fast and Simple</h3><p>Sed ut perspiciatis unde omnis iste natus error sit voluptatem accusantium doloremque laudantium, totam rem aperiam, eaque ipsa quae ab illo inventore veritatis et quasi architecto</p><div class="meta"><span class="stars">★★★★★</span>| 8 Minutes Ago</div></article>
<article class="review featured" style="left:442px;padding-top:14px"><h3>It was much better than<br>I anticipated</h3><p>Sed ut perspiciatis unde omnis iste natus error sit voluptatem accusantium doloremque laudantium, totam rem aperiam, eaque ipsa quae ab illo inventore veritatis et quasi architecto</p><div class="meta"><span class="stars">★★★★★</span>| 8 Minutes Ago</div></article>
<article class="review" style="left:789px"><h3>Cash on the spot!</h3><p>Sed ut perspiciatis unde omnis iste natus error sit voluptatem accusantium doloremque laudantium, totam rem aperiam, eaque ipsa quae ab illo inventore veritatis et quasi architecto</p><div class="meta"><span class="stars">★★★★★</span>| 8 Minutes Ago</div></article>

<footer class="site-footer">
  <div class="f-col" style="left:93px"><h4>Sitemap</h4><ul><li>Home</li><li>About Us</li><li>Service</li><li>Contact Us</li></ul></div>
  <div class="f-col" style="left:262px"><h4>Instant Offer</h4><ul><li>Trusted Buyer</li><li>Thousands of Happy Seller</li><li>Get an offer instantly Online!</li></ul></div>
  <div class="f-col" style="left:506px"><h4>Contact Us</h4>
    <div class="f-contact"><svg width="9" height="12" viewBox="0 0 9 12"><path d="M4.5 0A4.5 4.5 0 0 0 0 4.5C0 8 4.5 12 4.5 12S9 8 9 4.5A4.5 4.5 0 0 0 4.5 0z" fill="#74c230"/></svg><span>15M/ Lorem ipsum dolar sit amet<br>Glassglow 25 USA</span></div>
    <div class="f-contact"><svg width="10" height="12" viewBox="0 0 24 24"><path fill="#74c230" d="M6.6 10.8a15 15 0 0 0 6.6 6.6l2.2-2.2c.3-.3.7-.4 1-.2 1.1.4 2.3.6 3.6.6.6 0 1 .4 1 1V20c0 .6-.4 1-1 1A17 17 0 0 1 3 4c0-.6.4-1 1-1h3.5c.6 0 1 .4 1 1 0 1.3.2 2.5.6 3.6.1.3 0 .7-.2 1z"/></svg><span>+1 (555) 014 2297</span></div>
    <div class="f-contact"><svg width="11" height="12" viewBox="0 0 11 8"><rect width="11" height="8" fill="#74c230"/><path d="M0 0l5.5 4L11 0" stroke="#1b1b1b" fill="none"/></svg><span>hello@favorzo.com</span></div>
  </div>
  <div class="f-col" style="left:759px"><h4>Reach Us</h4></div>
  <div class="field" style="left:759px;top:104px;width:171px;height:29px">Name:</div>
  <div class="field" style="left:759px;top:139px;width:171px;height:30px">Email:</div>
  <div class="field" style="left:759px;top:175px;width:171px;height:29px">Phone:</div>
  <div class="field" style="left:934px;top:104px;width:172px;height:100px">Comments:</div>
  <div class="btn btn-green" style="left:1036px;top:210px;width:70px;height:31px;font-size:10.5px">Send</div>
  <div class="socials"><span></span><span></span><span></span><span></span></div>
  <div class="copyright">COPYRIGHT © 2020 <em>FAVORZO AUTO RECYCLING</em>. ALL RIGHTS RESERVED.</div>
</footer>

</body>
</html>
```